Lanterns After Rain - CD cover indie music

This is my 4th and final album. I am sharing my story of trials, pain and persistence that led me here, like a sound track to a short film.
I would like a design that communicates both a painful phase of life, yet tranquility and beauty found as life winds down. Can be illustrated or photograph.
On front design should have title 'Lanterns After Rain' and artist name.
I will need to add credits and song list.
I am thinking a booklet will be added with lyrics and a few photos and plan to work with this artist. Thank you

Target Market(s)

Folk, easy listening, story telling

Industry/Entity Type

Indie music - independent

Font styles to use
Sans Serif
Other font styles liked:
• I like also verdana font.

Requirements
Nice to have
• a contrast of colors to emotions may work well. There is a portuguese word ‘saudade’ that expresses sadness, but longing also.
Should not have
• No bright red. Not busy. No images of people or animals.

```html
<!DOCTYPE html>
<html lang="en">
<head>
<meta charset="utf-8">
<title>Lanterns After Rain — Album Cover</title>
<link rel="stylesheet" href="https://fonts.googleapis.com/css2?family=Montserrat:wght@700;800&family=Rozha+One&display=swap">
<style>
  :root {
    --blue-deep: #1c4f86;
    --blue-light: #2f7aa6;
    --navy: #262b5e;
    --violet: #3b2b68;
    --plum: #7e1f58;
    --orange: #e8721c;
    --amber: #f2ae2c;
    --salmon: #ee8a74;
    --rose: #d8699a;
    --dusk: #4a2d70;
    --cobalt: #1f4ea0;
    --teal: #1f5766;
    --ink: #0b0b14;
    --white: #ffffff;
  }
  * { margin: 0; padding: 0; box-sizing: border-box; }
  html, body {
    width: 1200px;
    height: 1200px;
    overflow: hidden;
    background: var(--navy);
  }
  .cover {
    position: relative;
    width: 1200px;
    height: 1200px;
    overflow: hidden;
  }
  .cover-art {
    position: absolute;
    inset: 0;
    background:
      linear-gradient(180deg, rgba(20, 22, 60, 0.55) 0%, rgba(20, 22, 60, 0) 30%, rgba(20, 22, 60, 0) 100%),
      linear-gradient(90deg,
        var(--blue-deep) 0%,
        var(--blue-light) 11%,
        var(--navy) 17%,
        var(--violet) 24%,
        var(--plum) 30%,
        var(--orange) 37%,
        var(--amber) 48%,
        var(--salmon) 58%,
        var(--rose) 65%,
        var(--dusk) 73%,
        var(--navy) 80%,
        var(--cobalt) 88%,
        var(--teal) 100%);
  }
  .title-block {
    position: absolute;
    left: 0;
    right: 0;
    top: 888px;
    text-align: center;
    color: var(--white);
  }
  .title-lead {
    font-family: "Montserrat", Verdana, sans-serif;
    font-weight: 800;
    font-size: 58px;
    line-height: 1;
    letter-spacing: -0.5px;
    text-transform: uppercase;
    text-shadow: 3px 3px 0 var(--ink);
  }
  .title-main {
    margin-top: 8px;
    font-family: "Rozha One", Georgia, serif;
    font-size: 118px;
    line-height: 1;
    letter-spacing: 1px;
    text-transform: uppercase;
    text-shadow: 4px 4px 0 var(--ink);
  }
  .artist-name {
    position: absolute;
    left: 0;
    right: 0;
    top: 1114px;
    text-align: center;
    color: var(--white);
    font-family: "Montserrat", Verdana, sans-serif;
    font-weight: 700;
    font-size: 33px;
    line-height: 1;
    letter-spacing: 11px;
    text-transform: uppercase;
    text-shadow: 3px 3px 0 var(--ink);
  }
</style>
</head>
<body>
  <main class="cover">
    <div class="cover-art" role="img" aria-label="Painted artwork of nested rounded archways in blue and violet, opening onto a glowing corridor of orange, gold and pink with a pale moon and a winding path"></div>
    <h1 class="title-block">
      <span class="title-lead">Lanterns After</span><br>
      <span class="title-main">Rain</span>
    </h1>
    <p class="artist-name">Artist Name</p>
  </main>
</body>
</html>
```